Teilnehmerzertifikat für Expeditionsmobil
Zielgruppe
Wir bitten alles Rund um das Thema Expeditionsmobil an. Unter anderem unsere Lagerfeuer und Weite Fahrt nach Tunesien und dafür benötige ich ein Teilnehmer Zertifikat.
Aufgabenstellung
Im Hintergrund soll ein Bild von der Sahara verarbeitet sein und im Vordergrund möchte ich von jedem Teilnehmer ein Bild mit dem eigenen Expeditonsfahrzeug einfügen. Das Zertifikat soll persöhnlich und wie von einem Freund sein

```html
<!DOCTYPE html>
<html lang="de">
<head>
<meta charset="utf-8">
<title>Teilnehmerzertifikat Tunesien</title>
<link href="https://fonts.googleapis.com/css2?family=Poppins:wght@700;800&family=Barlow:wght@500;600&display=swap" rel="stylesheet">
<style>
  :root {
    --ground: #433638;
    --sage: #8b9a80;
    --white: #ffffff;
    --gold: #c9a46a;
    --sky: #8fb3cf;
    --sand: #c9a679;
    --scrub: #8c7b58;
  }
  html, body { margin: 0; padding: 0; overflow: hidden; background: var(--ground); }
  .certificate {
    position: relative;
    width: 849px; height: 1200px;
    background: var(--ground);
    overflow: hidden;
    font-family: "Barlow", sans-serif;
  }
  .backdrop { position: absolute; inset: 0; }
  .name {
    position: absolute; left: 58px; margin: 0;
    font-family: "Poppins", sans-serif; font-weight: 800; line-height: 1;
  }
  .name--first { top: 50px; font-size: 104px; color: var(--sage); letter-spacing: 2px; }
  .name--last { top: 160px; font-size: 74px; color: var(--white); font-weight: 700; letter-spacing: 1px; }
  .photo-label {
    position: absolute; left: 698px; top: 294px;
    font-family: "Poppins", sans-serif; font-weight: 700; font-size: 28px; color: #1d1718;
  }
  .message {
    position: absolute; left: 55px; top: 740px; margin: 0;
    font-size: 21px; line-height: 30.5px; letter-spacing: 1.3px; color: var(--white); font-weight: 500;
  }
  .place-date {
    position: absolute; left: 55px; top: 1055px;
    font-size: 17px; font-weight: 600; letter-spacing: .6px; color: var(--gold);
  }
  .signature-line { position: absolute; left: 452px; width: 178px; height: 1px; background: var(--white); }
  .signature-line--one { top: 1077px; }
  .signature-line--two { top: 1140px; }
  .tour-mark {
    position: absolute; left: 684px; top: 1030px; width: 130px;
    font-family: "Poppins", sans-serif; font-weight: 800; font-size: 21px; line-height: 1.05;
    color: var(--white); text-transform: uppercase;
  }
  .dot { position: absolute; width: 20px; height: 20px; border-radius: 50%; background: var(--white); }
</style>
</head>
<body>
<div class="certificate">
  <svg class="backdrop" width="849" height="1200" viewBox="0 0 849 1200">
    <defs>
      <linearGradient id="desert" x1="0" y1="0" x2="0" y2="1">
        <stop offset="0" stop-color="var(--sky)"/>
        <stop offset="0.22" stop-color="#d9d2c4"/>
        <stop offset="0.3" stop-color="var(--sand)"/>
        <stop offset="1" stop-color="var(--scrub)"/>
      </linearGradient>
    </defs>
    <path role="img" aria-label="Foto: Konvoi von Expeditionsmobilen auf einer Sandpiste durch die tunesische Wüste"
      fill="url(#desert)"
      d="M0,0 L442,0 C620,60 780,200 849,430 L849,720 C760,800 560,830 420,808 C200,760 90,640 0,534 Z"/>
    <rect x="0" y="24" width="849" height="4" fill="var(--white)"/>
    <g class="sweep-lines" fill="none" stroke="var(--white)" stroke-width="2.5">
      <path d="M0,280 C150,250 340,235 545,245"/>
      <path d="M0,292 C150,262 340,247 545,257"/>
      <path d="M0,304 C150,274 340,259 545,269"/>
      <path d="M0,316 C150,286 340,271 545,281"/>
      <path d="M0,328 C150,298 340,283 545,293"/>
      <path d="M0,340 C150,310 340,295 545,305"/>
      <path d="M540,420 C640,425 760,440 849,470"/>
      <path d="M540,432 C640,437 760,452 849,482"/>
      <path d="M540,444 C640,449 760,464 849,494"/>
      <path d="M540,456 C640,461 760,476 849,506"/>
    </g>
    <polygon points="612,166 849,198 849,208 620,178 592,372 582,370" fill="var(--white)"/>
    <polygon points="627,192 849,228 849,392 591,370" fill="var(--white)"/>
  </svg>

  <h1 class="name name--first">Vorname</h1>
  <h2 class="name name--last">Nachname</h2>
  <div class="photo-label">Foto</div>

  <p class="message">
    Ihr habt mit<br>
    Begeisterung und<br>
    Abenteuerlust an unserer<br>
    gemeinsamen Reise durch Tunesien teilgenommen.<br>
    Mit eurem Expeditionsmobil habt ihr die Wüste<br>
    bezwungen, neue Freundschaften geschlossen und die<br>
    Magie dieses einzigartigen Landes erlebt.<br>
    Danke, dass ihr Teil dieser besonderen Tour wart –<br>
    auf viele weitere Abenteuer!
  </p>

  <div class="place-date">Ort und Datum</div>
  <div class="signature-line signature-line--one"></div>
  <div class="signature-line signature-line--two"></div>

  <div class="tour-mark">Lagerfeuer und Weite Fahrt 2024</div>

  <span class="dot" style="left:2px;top:1108px"></span>
  <span class="dot" style="left:68px;top:1108px"></span>
  <span class="dot" style="left:136px;top:1108px"></span>
  <span class="dot" style="left:2px;top:1180px"></span>
  <span class="dot" style="left:68px;top:1180px"></span>
</div>
</body>
</html>
```